DL Flyer,A4 letterhead, with compliments slip, and envelopes
For new safety consultancy business
DL Flyer,A4 letterhead, with compliments slip, and envelopes - Consulting
Creative Brief
Yes
New safety consultancy in Australia, focussing on small to medium industrial businesses.
Modern
Unsure - similar to logo maybe?
DL size FLYER TO be one sided glossy to INCLUDE FOLLOWING WORDS:
Occupational Health and Safety is a minefield of laws and regulations for the unprepared employer. Did you know that no matter how small an employer you are, by law you still need a safety management system? Did you know that you need specific procedures in place to prove that your employees, contractors and visitors are safe?
Let Hazardwell implement an OHS strategy that is cost effective and right for you.
Our services not only include OHS advice but also the development of:
- OHS management systems
- Risk assessments
- Safe work method statements
- Checklists, forms and registers
- Training and toolbox talks
Hazardwell is a local business, accredited in auditing Australian Standard 4801 OHS management systems. To arrange a free OHS pulse check of your systems and find out if you meet legislation, call Hazardwell now on 0418 264 907.
info@hazardwellexample.com.au
www.hazardwellexample.com.au
LETTER HEAD TO INCLUDE following company details:
Company name: Hazardwell
Address: PO Box 58, Brindlemoor NSW 2391
Phone: 0418 264 907
Email: info@hazardwellexample.com.au
Web: www.hazardwellexample.com.au

```html
<!DOCTYPE html>
<html lang="en">
<head>
<meta charset="utf-8">
<title>Hazardwell Stationery Suite</title>
<link rel="stylesheet" href="https://fonts.googleapis.com/css2?family=Open+Sans:wght@400;600;800&family=Great+Vibes&display=swap">
<style>
  :root {
    --bg: #e9e6e1;
    --paper: #ffffff;
    --green: #5f9a1e;
    --orange: #f08a00;
    --yellow: #fbc21a;
    --charcoal: #1f1f1f;
    --ink: #4a4a4a;
    --muted: #8a8a8a;
    --water-top: #4f8fb5;
    --water-bottom: #1d4d6e;
  }
  * { box-sizing: border-box; margin: 0; padding: 0; }
  html, body { width: 1200px; height: 514px; overflow: hidden; }
  body {
    position: relative;
    background: var(--bg);
    font-family: "Open Sans", Arial, sans-serif;
    color: var(--ink);
  }
  .piece {
    position: absolute;
    background: var(--paper);
    box-shadow: 0 2px 6px rgba(0,0,0,.18);
    overflow: hidden;
  }
  .brand {
    font-family: "Open Sans", Arial, sans-serif;
    font-weight: 800;
    color: var(--green);
    letter-spacing: -0.02em;
    line-height: 1;
    display: flex;
    align-items: center;
    gap: .3em;
  }
  .brand-mark {
    width: .7em; height: .7em;
    background: var(--green);
    display: inline-block;
  }
  .brand.on-dark { color: var(--yellow); }
  .brand.on-dark .brand-mark { background: var(--yellow); }
  .tab {
    position: absolute;
    bottom: 0;
    clip-path: polygon(50% 0, 100% 100%, 0 100%);
    background: linear-gradient(180deg, var(--yellow), var(--orange));
  }
  .footer-line {
    position: absolute;
    font-size: 4px;
    color: var(--muted);
    white-space: nowrap;
  }

  /* Business cards */
  .card-back { left: 24px; top: 204px; width: 156px; height: 80px; }
  .card-back .brand { position: absolute; left: 12px; top: 28px; font-size: 17px; }
  .card-back .tab { right: 14px; width: 34px; height: 18px; }

  .card-front {
    left: 29px; top: 296px; width: 152px; height: 80px;
    background: linear-gradient(120deg, var(--yellow) 0%, var(--orange) 70%, #e36f00 100%);
  }
  .card-front .brand { position: absolute; left: 30px; top: 24px; font-size: 17px; color: var(--charcoal); }
  .card-front .brand .brand-mark { background: var(--charcoal); }
  .card-front .card-web { position: absolute; left: 30px; top: 56px; font-size: 5px; color: var(--charcoal); }

  /* Compliments slip */
  .comp-slip { left: 24px; top: 392px; width: 163px; height: 112px; }
  .comp-slip .brand { position: absolute; left: 10px; top: 10px; font-size: 11px; }
  .comp-slip .comp-title {
    position: absolute; left: 12px; top: 46px;
    font-family: "Great Vibes", cursive; font-size: 15px; color: var(--ink);
  }
  .comp-slip .tab { left: 64px; width: 36px; height: 18px; bottom: 10px; }
  .comp-slip .footer-line { left: 0; right: 0; bottom: 3px; text-align: center; font-size: 3.4px; }

  /* Letterhead */
  .letterhead { left: 307px; top: 84px; width: 250px; height: 420px; }
  .letterhead .brand { position: absolute; left: 16px; top: 22px; font-size: 20px; }
  .letterhead .tab { left: 100px; width: 50px; height: 26px; bottom: 16px; }
  .letterhead .footer-line { left: 0; right: 0; bottom: 6px; text-align: center; }

  /* DL flyer */
  .flyer {
    left: 629px; top: 156px; width: 96px; height: 288px;
    background: linear-gradient(180deg, var(--charcoal) 0%, #2b2b2b 40%, var(--orange) 78%, var(--yellow) 100%);
    color: #f2f2f2;
  }
  .flyer .brand { position: absolute; left: 8px; top: 10px; font-size: 11px; }
  .flyer-body {
    position: absolute; left: 8px; right: 8px; top: 32px;
    font-size: 3.1px; line-height: 1.35;
  }
  .flyer-body p { margin-bottom: 2px; }
  .flyer-body ul { list-style: none; margin-bottom: 2px; }
  .flyer-body li::before { content: "✓ "; color: var(--yellow); }
  .flyer-phone { position: absolute; left: 8px; right: 8px; top: 196px; font-size: 6px; font-weight: 800; color: var(--charcoal); text-align: center; }
  .flyer-photo {
    position: absolute; left: 8px; right: 8px; top: 212px; height: 56px;
    background: linear-gradient(180deg, var(--water-top), var(--water-bottom));
  }
  .flyer-contact { position: absolute; left: 0; right: 0; bottom: 5px; text-align: center; font-size: 3.2px; color: var(--charcoal); }

  /* Envelopes */
  .envelope { left: 866px; width: 310px; height: 90px; }
  .envelope .brand { position: absolute; left: 14px; top: 12px; font-size: 13px; }
  .envelope .tab { width: 34px; height: 18px; right: 20px; }
  .envelope .footer-line { right: 62px; bottom: 4px; font-size: 3.6px; }

  .envelope-back { top: 206px; background: var(--paper); }
  .envelope-back .flap {
    position: absolute; left: 0; top: 0; width: 100%; height: 40px;
    background: var(--charcoal);
  }
  .envelope-back .brand { left: 116px; top: 14px; }

  .envelope-banded { top: 312px; }
  .envelope-banded .band {
    position: absolute; left: 0; top: 0; width: 100%; height: 30px;
    background: linear-gradient(90deg, var(--yellow), var(--orange));
  }
  .envelope-banded .brand { top: 42px; }

  .envelope-plain { top: 418px; }
</style>
</head>
<body>

  <div class="piece card-back">
    <div class="brand"><span class="brand-mark"></span>Hazardwell</div>
    <div class="tab"></div>
  </div>

  <div class="piece card-front">
    <div class="brand"><span class="brand-mark"></span>Hazardwell</div>
    <div class="card-web">www.hazardwellexample.com.au</div>
  </div>

  <div class="piece comp-slip">
    <div class="brand"><span class="brand-mark"></span>Hazardwell</div>
    <div class="comp-title">With Compliments</div>
    <div class="tab"></div>
    <div class="footer-line">PO Box 58, Brindlemoor NSW 2391 · 0418 264 907 · info@hazardwellexample.com.au</div>
  </div>

  <div class="piece letterhead">
    <div class="brand"><span class="brand-mark"></span>Hazardwell</div>
    <div class="tab"></div>
    <div class="footer-line">PO Box 58, Brindlemoor NSW 2391 · 0418 264 907 · info@hazardwellexample.com.au · www.hazardwellexample.com.au</div>
  </div>

  <div class="piece flyer">
    <div class="brand on-dark"><span class="brand-mark"></span>Hazardwell</div>
    <div class="flyer-body">
      <p>Occupational Health and Safety is a minefield of laws and regulations for the unprepared employer. Did you know that no matter how small an employer you are, by law you still need a safety management system? Did you know that you need specific procedures in place to prove that your employees, contractors and visitors are safe?</p>
      <p>Let Hazardwell implement an OHS strategy that is cost effective and right for you.</p>
      <p>Our services not only include OHS advice but also the development of:</p>
      <ul>
        <li>OHS management systems</li>
        <li>Risk assessments</li>
        <li>Safe work method statements</li>
        <li>Checklists, forms and registers</li>
        <li>Training and toolbox talks</li>
      </ul>
      <p>Hazardwell is a local business, accredited in auditing Australian Standard 4801 OHS management systems. To arrange a free OHS pulse check of your systems and find out if you meet legislation, call Hazardwell now on 0418 264 907.</p>
    </div>
    <div class="flyer-phone">0418 264 907</div>
    <div class="flyer-photo" role="img" aria-label="Photo of a life ring floating on blue water"></div>
    <div class="flyer-contact">info@hazardwellexample.com.au<br>www.hazardwellexample.com.au</div>
  </div>

  <div class="piece envelope envelope-back">
    <div class="flap"></div>
    <div class="brand on-dark"><span class="brand-mark"></span>Hazardwell</div>
  </div>

  <div class="piece envelope envelope-banded">
    <div class="band"></div>
    <div class="brand"><span class="brand-mark"></span>Hazardwell</div>
    <div class="tab"></div>
    <div class="footer-line">PO Box 58, Brindlemoor NSW 2391 · www.hazardwellexample.com.au</div>
  </div>

  <div class="piece envelope envelope-plain">
    <div class="brand"><span class="brand-mark"></span>Hazardwell</div>
    <div class="tab"></div>
    <div class="footer-line">PO Box 58, Brindlemoor NSW 2391 · www.hazardwellexample.com.au</div>
  </div>

</body>
</html>
```